Business Process / Lifecycle Diagram for Consulting Firm

We are a Delaware-based business modernization and transition-readiness firm. We need a clean, professional process diagram that visually represents our client lifecycle. This is not a marketing funnel or sales graphic — it is a product and delivery lifecycle.

The diagram must be reusable across pitch decks, one-pagers, grant applications, and our website.

Required Structure (must follow exactly)
Stage 1 — Diagnose
Enterprise Upgrade Audit (EUA)
Shift Preparedness Gauge™ (SPG)
(Parallel entry points, equal visual weight)

→ Output: Diagnostic Insight & Priority Signals

Stage 2 — Clarify
Modernization Roadmap (Co-Created)

Stage 3 — Modernize
Q7 — Margin & Momentum Track

Stage 4 — Sustain
Ongoing Modernization Support

Foundation Layer (supports all stages)
HRG-OS™ pillars: People, Process, Systems, Insight

End Outcome
- Operational Clarity
- Sustainable Profitability
- Long-Term Stability

Design Requirements
- Professional, calm (not startup / SaaS style)
- Minimal text, clear hierarchy
- Horizontal or left-to-right flow preferred
- No funnels, no sales language, no aggressive arrows
- Must be delivered as editable vector (AI, SVG, or Figma)

Brand Notes
- Neutral color palette that complements logo attached (Gold Color Code C39E11, Navy Blue code 002C55)
- One accent color for emphasis
- Clean typography
- Should feel credible to business owners, advisors, and lenders
- See website (https://www.hazelmereridgegroup.com/) and LinkedIn (https://www.hazelmereridgegroup.com/) for additional insight into branding.

What NOT to Do
- Do not rename stages
- Do not combine stages
- Do not add extra steps

```html
<!DOCTYPE html>
<html lang="en">
<head>
<meta charset="utf-8">
<title>Hazelmere Ridge Group — Client Lifecycle</title>
<link href="https://fonts.googleapis.com/css2?family=Barlow:wght@500;600&family=Barlow+Condensed:wght@600;700&display=swap" rel="stylesheet">
<style>
  :root{
    --gold:#c39e11;
    --gold-soft:#c8a74a;
    --navy:#15294d;
    --slate-1:#3e5070;
    --slate-2:#5a6a88;
    --slate-3:#7e8aa0;
    --pale:#e6edf6;
    --pale-line:#c9d3e1;
    --line:#9aa3b2;
    --white:#ffffff;
    --bg:#ffffff;
  }
  *{margin:0;padding:0;box-sizing:border-box}
  html,body{width:1200px;height:523px;overflow:hidden;background:var(--bg)}
  .canvas{
    position:absolute;left:0;top:0;width:1160px;height:490px;
    transform:scale(1.0345,1.0673);transform-origin:0 0;
    font-family:"Barlow",sans-serif;
  }
  .abs{position:absolute}
  .brand{left:470px;top:48px;display:flex;align-items:center;gap:10px}
  .brand-mark{width:14px;height:14px;background:var(--gold)}
  .brand-name{font-family:"Barlow",sans-serif;font-weight:600;color:var(--navy);font-size:19px;letter-spacing:.06em;line-height:1.05}

  .stage{
    height:27px;top:155px;border-radius:4px;background:var(--gold);color:var(--white);
    font-family:"Barlow Condensed",sans-serif;font-weight:700;font-size:19px;letter-spacing:.02em;
    display:flex;align-items:center;justify-content:center;
  }
  .stage.outcome{background:var(--slate-1);border-radius:14px}

  .step{
    top:189px;height:65px;color:var(--white);font-size:10.5px;font-weight:500;line-height:1.35;
    display:flex;align-items:center;justify-content:center;text-align:center;padding:0 8px;
  }
  .step.diag{background:var(--navy)}
  .step.clarify{background:var(--slate-1)}
  .step.modern{background:var(--slate-2)}
  .step.sustain{background:var(--slate-3)}

  .signal{
    left:333px;width:84px;height:15px;background:var(--pale);color:var(--navy);
    font-size:8.5px;font-weight:600;display:flex;align-items:center;justify-content:center;
  }

  .outcomes{
    left:923px;top:189px;width:201px;height:65px;background:var(--pale);
    list-style:none;padding:9px 0 0 13px;
  }
  .outcomes li{
    font-family:"Barlow Condensed",sans-serif;font-weight:700;font-size:12px;color:var(--navy);
    letter-spacing:.03em;line-height:16px;display:flex;align-items:center;gap:7px;
  }
  .outcomes li::before{content:"";width:6px;height:6px;border-radius:50%;background:var(--slate-1)}

  .foundation{left:73px;top:260px;width:814px;height:5px;background:var(--gold)}
  .pillar-label{
    font-family:"Barlow Condensed",sans-serif;font-weight:700;font-size:10px;fill:var(--white);letter-spacing:.06em;
  }
  svg.overlay{position:absolute;left:0;top:0}
</style>
</head>
<body>
<div class="canvas">

  <div class="abs brand">
    <span class="brand-mark"></span>
    <span class="brand-name">HAZELMERE<br>RIDGE GROUP</span>
  </div>

  <svg class="overlay" width="1160" height="490" viewBox="0 0 1160 490" aria-hidden="true">
    <defs>
      <marker id="tip" markerWidth="8" markerHeight="8" refX="7" refY="4" orient="auto">
        <path d="M0,0 L7,4 L0,8" fill="none" stroke="var(--line)" stroke-width="1"/>
      </marker>
    </defs>
    <g stroke="var(--line)" stroke-width="1" fill="none">
      <line x1="250" y1="168" x2="462" y2="168" marker-end="url(#tip)"/>
      <line x1="543" y1="168" x2="602" y2="168" marker-end="url(#tip)"/>
      <line x1="722" y1="168" x2="776" y2="168" marker-end="url(#tip)"/>
      <line x1="866" y1="168" x2="951" y2="168" marker-end="url(#tip)"/>
      <path d="M418,212 H430 V233 H418"/>
      <line x1="430" y1="222" x2="442" y2="222"/>
      <line x1="567" y1="222" x2="601" y2="222"/>
      <line x1="727" y1="222" x2="762" y2="222"/>
      <line x1="888" y1="222" x2="917" y2="222" marker-end="url(#tip)"/>
    </g>

    <g id="pillars">
      <g transform="translate(200,0)" fill="var(--navy)">
        <rect x="-19" y="270" width="38" height="7"/><rect x="-13" y="277" width="26" height="4"/>
        <rect x="-10" y="281" width="20" height="64"/>
        <rect x="-13" y="345" width="26" height="5"/><rect x="-19" y="350" width="38" height="10"/>
        <text class="pillar-label" transform="translate(4,313) rotate(-90)" text-anchor="middle">PEOPLE</text>
      </g>
      <g transform="translate(505,0)" fill="var(--slate-1)">
        <rect x="-19" y="270" width="38" height="7"/><rect x="-13" y="277" width="26" height="4"/>
        <rect x="-10" y="281" width="20" height="64"/>
        <rect x="-13" y="345" width="26" height="5"/><rect x="-19" y="350" width="38" height="10"/>
        <text class="pillar-label" transform="translate(4,313) rotate(-90)" text-anchor="middle">PROCESS</text>
      </g>
      <g transform="translate(665,0)" fill="var(--slate-2)">
        <rect x="-19" y="270" width="38" height="7"/><rect x="-13" y="277" width="26" height="4"/>
        <rect x="-10" y="281" width="20" height="64"/>
        <rect x="-13" y="345" width="26" height="5"/><rect x="-19" y="350" width="38" height="10"/>
        <text class="pillar-label" transform="translate(4,313) rotate(-90)" text-anchor="middle">SYSTEMS</text>
      </g>
      <g transform="translate(825,0)" fill="var(--slate-3)">
        <rect x="-19" y="270" width="38" height="7"/><rect x="-13" y="277" width="26" height="4"/>
        <rect x="-10" y="281" width="20" height="64"/>
        <rect x="-13" y="345" width="26" height="5"/><rect x="-19" y="350" width="38" height="10"/>
        <text class="pillar-label" transform="translate(4,313) rotate(-90)" text-anchor="middle">INSIGHT</text>
      </g>
    </g>

    <g id="icons" fill="none" stroke="var(--gold-soft)" stroke-width="2" stroke-linecap="round" stroke-linejoin="round">
      <!-- people -->
      <circle cx="186" cy="384" r="6"/><circle cx="202" cy="380" r="7"/><circle cx="218" cy="384" r="6"/>
      <path d="M172,410 v-7 a9,9 0 0 1 16,-6"/>
      <path d="M232,410 v-7 a9,9 0 0 0 -16,-6"/>
      <path d="M187,410 v-8 a15,13 0 0 1 30,0 v8 z"/>
      <!-- cycle -->
      <path d="M485,388 a20,20 0 0 1 36,-4"/><path d="M521,376 v8 h-8"/>
      <path d="M525,400 a20,20 0 0 1 -36,4"/><path d="M489,412 v-8 h8"/>
      <!-- hierarchy -->
      <rect x="656" y="376" width="18" height="12"/>
      <rect x="634" y="406" width="18" height="13"/><rect x="678" y="406" width="18" height="13"/>
      <path d="M665,388 v8 M643,406 v-10 h44 v10"/>
      <!-- lightbulb -->
      <path d="M816,406 v-4 a15,15 0 1 1 18,0 v4 z"/>
      <path d="M818,411 h14 M820,416 h10"/>
      <path d="M825,368 v-6 M804,376 l-4,-4 M846,376 l4,-4 M797,392 h-6 M853,392 h6"/>
    </g>
  </svg>

  <div class="abs stage" style="left:152px;width:96px">DIAGNOSE</div>
  <div class="abs stage" style="left:468px;width:73px">CLARIFY</div>
  <div class="abs stage" style="left:608px;width:112px">MODERNIZE</div>
  <div class="abs stage" style="left:782px;width:82px">SUSTAIN</div>
  <div class="abs stage outcome" style="left:957px;width:135px">END OUTCOME</div>

  <div class="abs step diag" style="left:73px;width:122px">Enterprise Upgrade<br>Audit (EUA)</div>
  <div class="abs step diag" style="left:202px;width:124px">Shift Preparedness<br>Gauge™ (SPG)</div>
  <div class="abs signal" style="top:205px">Diagnostic Insight</div>
  <div class="abs signal" style="top:225px">Priority Signals</div>
  <div class="abs step clarify" style="left:442px;width:125px">Modernization Roadmap<br>(Co-Created)</div>
  <div class="abs step modern" style="left:601px;width:126px">Q7 Margin &amp;<br>Momentum Track</div>
  <div class="abs step sustain" style="left:762px;width:124px">Ongoing Modernization<br>Support</div>

  <ul class="abs outcomes">
    <li>OPERATIONAL CLARITY</li>
    <li>SUSTAINABLE PROFITABILITY</li>
    <li>LONG-TERM STABILITY</li>
  </ul>

  <div class="abs foundation"></div>
</div>
</body>
</html>
```